Unique and original Business Card for Financial Services Business

I have moved premises and need to change the detail on my business card so thought now is a good time for a re-design. Looking for something professional and modern with colours to fit in with out logo. Like the idea of foil or embossing if that works but not a must have but I do want something that stands out and that I could not design myself.

Once business card is designed I will also be looking to get letterhead and flyers done but want the business card concept in place first.

The majority of designs I am receiving are generic and template based. I am looking for something unique and original. We have some great design elements in our logo, think outside the box and show me something that stands out from the crowd.

Target Market(s)

Business Professionals

Industry/Entity Type

Finance

Contact Information for Business Card

Name: Delia Norwood Phone 0473 958 162 Address PO Box 8617 Mossvale NSW 2389 Email info@steadyharbourfinancialservices.com.au website www.steadyharbourfinancialservices.com.au

Font styles to use
Other font styles liked:
• Ralway

Requirements
Should not have
• No black backgrounds please

```html
<!DOCTYPE html>
<html lang="en">
<head>
<meta charset="utf-8">
<title>Steady Harbour Financial Services – Business Card</title>
<link rel="stylesheet" href="https://fonts.googleapis.com/css2?family=Raleway:wght@300;700&display=swap">
<style>
  :root {
    --stage: #ebebeb;
    --teal-bright: #10a89d;
    --teal-mid: #0b8a8c;
    --teal-deep: #0a6a78;
    --teal-night: #063343;
    --band: #1d9aa3;
    --ink: #ffffff;
    --ink-soft: rgba(255,255,255,0.85);
    --art-light: #f4f8f8;
    --art-tint: #bfe3e1;
  }
  * { box-sizing: border-box; margin: 0; padding: 0; }
  html, body { width: 1200px; height: 802px; overflow: hidden; }
  body {
    background: var(--stage);
    font-family: "Raleway", Arial, sans-serif;
    color: var(--ink);
    position: relative;
  }
  .card {
    position: absolute;
    top: 236px;
    width: 540px;
    height: 330px;
    overflow: hidden;
    box-shadow: 0 10px 24px rgba(0,0,0,0.18);
  }
  /* front */
  .card-front {
    left: 36px;
    background: linear-gradient(180deg, var(--teal-bright) 0%, var(--teal-mid) 55%, var(--teal-deep) 100%);
  }
  .front-shapes { position: absolute; inset: 0; }
  .brand-front {
    position: absolute;
    top: 26px;
    left: 190px;
    font-weight: 300;
  }
  .brand-name { font-size: 33px; letter-spacing: 0.5px; line-height: 1; }
  .brand-tag { font-size: 15px; letter-spacing: 7.5px; margin-top: 4px; }
  .holder {
    position: absolute;
    top: 104px;
    right: 28px;
    font-size: 17px;
    font-weight: 700;
    letter-spacing: 0.5px;
  }
  .address {
    position: absolute;
    top: 134px;
    right: 28px;
    text-align: right;
    font-family: Arial, Helvetica, sans-serif;
    font-size: 13px;
    line-height: 17px;
  }
  .contact-list {
    position: absolute;
    top: 182px;
    right: 22px;
    list-style: none;
    font-family: Arial, Helvetica, sans-serif;
    font-size: 12px;
    line-height: 18px;
    text-align: right;
  }
  .contact-list li { display: flex; justify-content: flex-end; align-items: center; gap: 6px; }
  .contact-list svg { width: 11px; height: 11px; fill: var(--ink); flex: none; }
  .online {
    position: absolute;
    left: 262px;
    bottom: 24px;
    font-family: Arial, Helvetica, sans-serif;
    font-size: 11.5px;
    line-height: 16px;
    color: var(--ink-soft);
  }
  /* back */
  .card-back {
    left: 624px;
    background: linear-gradient(200deg, var(--teal-bright) 0%, var(--teal-deep) 50%, var(--teal-night) 100%);
    display: flex;
    align-items: center;
    justify-content: center;
  }
  .brand-back {
    display: flex;
    flex-direction: column;
    align-items: center;
    font-weight: 300;
  }
  .brand-mark {
    width: 62px; height: 62px;
    border-radius: 50%;
    background: var(--ink);
    margin-bottom: 14px;
  }
  .brand-back .brand-name { font-size: 38px; }
  .brand-back .brand-tag { font-size: 17px; letter-spacing: 9px; margin-top: 6px; }
</style>
</head>
<body>

<section class="card card-front">
  <svg class="front-shapes" viewBox="0 0 540 330" width="540" height="330">
    <defs>
      <linearGradient id="art-fill" x1="0" y1="0" x2="1" y2="1">
        <stop offset="0" stop-color="var(--art-light)"/>
        <stop offset="1" stop-color="var(--art-tint)"/>
      </linearGradient>
    </defs>
    <path class="wave-band" d="M0 330 L0 300 C150 260 330 230 540 250 L540 330 Z" fill="var(--band)" opacity="0.55"/>
    <path class="wave-line" d="M160 330 C260 250 400 235 540 232" fill="none" stroke="#ffffff" stroke-opacity="0.25" stroke-width="2"/>
    <rect class="illustration-area" role="img" aria-label="White silhouette illustration of a hummingbird among floral swirls"
      x="0" y="112" width="250" height="218" fill="url(#art-fill)"/>
  </svg>

  <div class="brand-front">
    <div class="brand-name">STEADY HARBOUR</div>
    <div class="brand-tag">Financial Services</div>
  </div>

  <p class="holder">DELIA NORWOOD</p>
  <p class="address">PO Box 8617<br>Mossvale NSW 2389</p>

  <ul class="contact-list">
    <li>0473 958 162
      <svg viewBox="0 0 24 24" aria-hidden="true"><path d="M6.6 10.8a15 15 0 0 0 6.6 6.6l2.2-2.2c.3-.3.7-.4 1-.2 1.1.4 2.3.6 3.6.6.6 0 1 .4 1 1V20c0 .6-.4 1-1 1A17 17 0 0 1 3 4c0-.6.4-1 1-1h3.5c.6 0 1 .4 1 1 0 1.3.2 2.5.6 3.6.1.3 0 .7-.2 1z"/></svg>
    </li>
    <li>info@steadyharbourfinancialservices.com.au
      <svg viewBox="0 0 24 24" aria-hidden="true"><path d="M2 5h20v14H2z M4 7v.5l8 5 8-5V7l-8 5z" fill-rule="evenodd"/></svg>
    </li>
    <li>www.steadyharbourfinancialservices.com.au
      <svg viewBox="0 0 24 24" aria-hidden="true"><circle cx="12" cy="12" r="10"/></svg>
    </li>
  </ul>

  <div class="online">
    <p>info@steadyharbourfinancialservices.com.au</p>
    <p>www.steadyharbourfinancialservices.com.au</p>
  </div>
</section>

<section class="card card-back">
  <div class="brand-back">
    <span class="brand-mark" aria-hidden="true"></span>
    <div class="brand-name">STEADY HARBOUR</div>
    <div class="brand-tag">Financial Services</div>
  </div>
</section>

</body>
</html>
```